Tactical Supply Company needing memorable business card design

Our tactical supply comapny is in need of a new business card design that will set us apart from the amateurs. We sell tactical gear ranging from backpacks and range bags to apparel and other gear. We are looking for a sharp design that incorporates our logo, website, and name. Our colors are white, red, and black, or any combination of the three, preferably red and black.
I have attached our logo with our name underneath but I have also edited that design with the logo incorporated next to the name (attached).

Target Market(s)

Law enforcement, military, tactical

Industry/Entity Type

Business

Contact Information for Business Card

Include www.fernhollowprovisions-demo.com

Colors
000000
ec1f27
ffffff

Requirements
Must have
• Our name, logo, and website. This is intended to be a memorable simple card, no name, address, email, or phone number info is necessary. Designs that do include this additional info will still be considered if they are absolutely spectacular.
Should not have
• A standard template design, I can create that in my own on Cardvellum. I am looking for a new, creative design that is completely unique to my company.

```html
<!DOCTYPE html>
<html lang="en">
<head>
<meta charset="utf-8">
<title>Fernhollow Provisions Business Cards</title>
<link rel="stylesheet" href="https://fonts.googleapis.com/css2?family=Tinos:wght@700&family=Open+Sans:wght@400;700&display=swap">
<style>
  :root {
    --bg: #2a2a2c;
    --card-black: #050505;
    --card-sheen: #1c1c1e;
    --brand-red: #ec1f27;
    --brand-red-dark: #b5141b;
    --white: #ffffff;
  }
  * { box-sizing: border-box; margin: 0; padding: 0; }
  html, body { width: 1200px; height: 800px; overflow: hidden; }
  body {
    background: var(--bg);
    display: flex;
    align-items: center;
    justify-content: center;
    gap: 50px;
  }
  .card {
    position: relative;
    width: 525px;
    height: 300px;
    border-radius: 22px;
    overflow: hidden;
    background: linear-gradient(160deg, var(--card-sheen) 0%, var(--card-black) 45%, var(--card-black) 100%);
    box-shadow: 0 18px 40px rgba(0,0,0,0.55);
  }
  .card__band {
    height: 58px;
    background: linear-gradient(180deg, var(--brand-red) 0%, var(--brand-red-dark) 100%);
    display: flex;
    align-items: center;
    justify-content: center;
  }
  .card__company {
    font-family: "Tinos", "Times New Roman", serif;
    font-weight: 700;
    font-size: 17px;
    letter-spacing: 0.5px;
    color: var(--white);
    text-transform: uppercase;
  }
  .card__rule {
    position: absolute;
    left: 40px;
    right: 40px;
    height: 1px;
    background: linear-gradient(90deg, transparent, var(--brand-red) 20%, var(--brand-red) 80%, transparent);
  }
  .card__rule--upper { top: 208px; }
  .card__rule--lower { top: 272px; }
  .card__website {
    position: absolute;
    left: 0; right: 0;
    top: 226px;
    text-align: center;
    font-family: "Open Sans", Arial, sans-serif;
    font-size: 19px;
    color: var(--white);
  }
  .brand {
    position: absolute;
    left: 0; right: 0;
    display: flex;
    align-items: center;
    justify-content: center;
    font-family: "Open Sans", Arial, sans-serif;
    font-weight: 700;
    color: var(--white);
    text-transform: uppercase;
  }
  .brand__mark {
    background: var(--brand-red);
    flex: none;
  }
  .brand--stacked {
    top: 76px;
    flex-direction: column;
    gap: 10px;
    font-size: 26px;
    letter-spacing: 1px;
  }
  .brand--stacked .brand__mark { width: 48px; height: 48px; }
  .brand--inline {
    top: 112px;
    gap: 16px;
    font-size: 30px;
    letter-spacing: 1px;
  }
  .brand--inline .brand__mark { width: 52px; height: 52px; }
</style>
</head>
<body>
  <article class="card card--stacked">
    <div class="card__band"><span class="card__company">Fernhollow Provisions Company</span></div>
    <div class="brand brand--stacked">
      <span class="brand__mark" aria-hidden="true"></span>
      <span class="brand__name">Fernhollow Provisions</span>
    </div>
    <div class="card__rule card__rule--upper"></div>
    <p class="card__website">www.fernhollowprovisions-demo.com</p>
    <div class="card__rule card__rule--lower"></div>
  </article>

  <article class="card card--inline">
    <div class="card__band"><span class="card__company">Fernhollow Provisions Company</span></div>
    <div class="brand brand--inline">
      <span class="brand__mark" aria-hidden="true"></span>
      <span class="brand__name">Fernhollow Provisions</span>
    </div>
    <div class="card__rule card__rule--upper"></div>
    <p class="card__website">www.fernhollowprovisions-demo.com</p>
    <div class="card__rule card__rule--lower"></div>
  </article>
</body>
</html>
```